Lanternfield Drinks business cards

We need a business card design for our new logo. The company is modern, progressive, professional, yet approachable. The key products are ready to drink bottles and cans of coffee based beverages.
These cards will be a critical part of the first impression made by our sales organization, business development team, and all external facing personnel.
Card can be a vertical or horizontal orientation.

Target Market(s)

Customers, suppliers, business partners

Industry/Entity Type

Business

Contact Information for Business Card

Business cards should feature Company Name and Logo.

Font styles to use
Serif

Colors

Designer to choose colors to be used in the design.

Requirements
Must have
• Strong readability of Name, phone #, mobile number and email address.
• Job title, website url, Street Address, and other details can be secondary level readability.
Nice to have
• High impact, simplistic quality design.
• Ok to utilize the 'H in the box' separate from the company name

```html
<!DOCTYPE html>
<html lang="en">
<head>
<meta charset="utf-8">
<title>Lanternfield Drinks business cards</title>
<link href="https://fonts.googleapis.com/css2?family=Crimson+Pro:wght@400;600;700&display=swap" rel="stylesheet">
<style>
  :root {
    --backdrop: #b9b9b9;
    --orange-top: #e08a3c;
    --orange-bottom: #c1502d;
    --brand-red: #c8462a;
    --paper: #f4f4f4;
    --paper-shade: #e6e6e6;
    --ink: #2b2b2b;
    --white: #ffffff;
  }
  * { box-sizing: border-box; margin: 0; padding: 0; }
  html, body { width: 1200px; height: 576px; overflow: hidden; }
  body {
    background: var(--backdrop);
    font-family: "Crimson Pro", Georgia, serif;
    position: relative;
  }
  .card {
    position: absolute;
    top: 138px;
    height: 294px;
    border-radius: 14px;
    overflow: hidden;
  }
  .card-front {
    left: 82px;
    width: 485px;
    background: linear-gradient(180deg, var(--orange-top) 0%, var(--orange-bottom) 100%);
  }
  .card-back {
    left: 602px;
    width: 480px;
    background: linear-gradient(160deg, var(--white) 0%, var(--paper) 50%, var(--paper-shade) 100%);
  }
  .brand-square {
    position: absolute;
    border-style: solid;
  }
  .card-front .brand-square {
    left: 204px; top: 78px; width: 76px; height: 76px;
    border-width: 4px; border-color: var(--white);
  }
  .card-front .brand-name {
    position: absolute;
    left: 0; right: 0; top: 172px;
    text-align: center;
    color: var(--white);
    font-weight: 700;
    font-size: 30px;
    letter-spacing: 0.5px;
    text-transform: uppercase;
  }
  .card-back .brand-square {
    left: 324px; top: 34px; width: 56px; height: 56px;
    border-width: 3px; border-color: var(--brand-red);
  }
  .card-back .brand-name {
    position: absolute;
    left: 250px; width: 206px; top: 104px;
    text-align: center;
    color: var(--brand-red);
    font-weight: 700;
    font-size: 17px;
    text-transform: uppercase;
    white-space: nowrap;
  }
  .holder-name {
    position: absolute; left: 22px; top: 34px;
    color: var(--brand-red);
    font-weight: 600; font-size: 20px;
  }
  .holder-title {
    position: absolute; left: 22px; top: 60px;
    color: var(--ink); font-size: 13px;
  }
  .contact-list {
    position: absolute; left: 22px; top: 176px;
    list-style: none;
  }
  .contact-list li {
    display: flex; align-items: center;
    height: 17px; font-size: 13.5px; color: var(--ink);
  }
  .contact-list svg { width: 11px; height: 11px; margin-right: 12px; fill: var(--brand-red); }
  .address {
    position: absolute; left: 22px; top: 250px;
    font-size: 13.5px; color: var(--ink);
  }
</style>
</head>
<body>
  <section class="card card-front">
    <div class="brand-square"></div>
    <div class="brand-name">Lanternfield Drinks</div>
  </section>

  <section class="card card-back">
    <div class="holder-name">John Doe Smith</div>
    <div class="holder-title">Managing Director</div>

    <div class="brand-square"></div>
    <div class="brand-name">Lanternfield Drinks</div>

    <ul class="contact-list">
      <li><svg viewBox="0 0 12 12"><path d="M1 4c0-2 2-3 5-3s5 1 5 3l-2 1-1-1.5H4L3 5zM2 6h8l1 5H1z"/></svg>555.555.5555</li>
      <li><svg viewBox="0 0 12 12"><path d="M3 0h6a1 1 0 0 1 1 1v10a1 1 0 0 1-1 1H3a1 1 0 0 1-1-1V1a1 1 0 0 1 1-1zm0 2v7h6V2z"/></svg>666.666.7777</li>
      <li><svg viewBox="0 0 12 12"><path d="M0 2h12v8H0zm1 1v.4l5 3.4 5-3.4V3z"/></svg>johndoe@yourwebsite.com</li>
      <li><svg viewBox="0 0 12 12"><path d="M6 0a6 6 0 1 0 0 12A6 6 0 0 0 6 0zm0 1.2c.8 0 1.6 2 1.7 4.2H4.3C4.4 3.2 5.2 1.2 6 1.2zM1.3 5.4h2c0-1.3.3-2.6.7-3.5a4.8 4.8 0 0 0-2.7 3.5zm7.4 0h2A4.8 4.8 0 0 0 8 1.9c.4.9.7 2.2.7 3.5zM1.3 6.6A4.8 4.8 0 0 0 4 10.1c-.4-.9-.7-2.2-.7-3.5zm3 0c.1 2.2.9 4.2 1.7 4.2s1.6-2 1.7-4.2zm4.4 0c0 1.3-.3 2.6-.7 3.5a4.8 4.8 0 0 0 2.7-3.5z"/></svg>www.yourwebsite.com</li>
    </ul>
    <div class="address">234 Anywhere St., Any Town, US 123456</div>
  </section>
</body>
</html>
```